Redesign Our Presentation on Rational Prescribing

We are looking for a new designer for QVMed, a project that creates educational modules for healthcare providers in the District of Columbia (more information at hlb.example-gov.org/qvmed). We want someone to redesign our powerpoints to look clean and professional, with original graphics that reflect the content on the slides. We also want someone who is creative and could potentially also redesign factsheets, written reports, and promotional postcards.

All the text on the slides must stay the same and it must be in the template (red line at the top, with the red box at the bottom, with the Harlow Bureau of Wellness logo). We want a powerpoint that features original graphics, looks professional, looks clean and is easy to read.

Industry/Entity Type

Healthcare

```html
<!DOCTYPE html>
<html lang="en">
<head>
<meta charset="utf-8">
<title>QVMed – Slide Design Ideas</title>
<link rel="stylesheet" href="https://fonts.googleapis.com/css2?family=Raleway:wght@300;400&family=Open+Sans:wght@400;600;700&family=Arimo:ital,wght@0,400;0,700;1,400;1,700&display=swap">
<style>
  :root {
    --board: #000000;
    --paper: #ffffff;
    --brand-red: #ff0000;
    --ink: #2b2b2b;
    --muted: #666666;
    --navy: #1a1a7a;
    --gold: #cc9900;
    --amber: #ffb900;
    --sky: #0e8fc4;
    --steel: #3a7ca5;
    --teal: #0b5676;
    --green: #00b04f;
    --cyan: #00aeef;
    --yellow: #ffff00;
  }
  * { box-sizing: border-box; margin: 0; padding: 0; }
  html, body { width: 1200px; height: 1200px; overflow: hidden; background: var(--board); }
  .board { position: relative; width: 1200px; height: 1200px; font-family: "Arimo", Arial, sans-serif; }
  .board-title {
    position: absolute; top: 50px; left: 0; width: 100%; text-align: center;
    font-family: "Raleway", sans-serif; font-weight: 400; font-size: 30px; color: #b9b9b9; letter-spacing: .5px;
  }
  .slide { position: absolute; width: 585px; height: 328px; background: var(--paper); overflow: hidden; }
  .slide > * { position: absolute; }
  .slide-title {
    left: 36px; top: 30px; font-family: "Open Sans", sans-serif; font-weight: 700; font-size: 14px; color: var(--ink); letter-spacing: .2px;
  }
  .brand { right: 16px; top: 16px; display: flex; align-items: center; gap: 5px; font-family: "Open Sans", sans-serif; font-weight: 700; font-size: 8.5px; color: var(--navy); line-height: 1.1; width: 92px; }
  .brand-mark { flex: none; width: 11px; height: 11px; background: var(--navy); }
  .rule { left: 36px; right: 0; top: 62px; height: 2px; background: var(--brand-red); }
  .footer { left: 0; right: 0; bottom: 0; height: 22px; background: var(--brand-red); color: #fff; display: flex; justify-content: space-between; align-items: center; padding: 0 22px 0 34px; font-size: 10.5px; }
  .footer .page { font-size: 8px; }
  .lede { left: 41px; top: 74px; width: 505px; font-size: 10.5px; color: var(--muted); line-height: 1.3; }
  .lede-bold { font-weight: 700; }

  /* slide 1 */
  .figure-art { left: 150px; top: 103px; width: 59px; height: 193px; border-radius: 28px 28px 8px 8px; background: linear-gradient(90deg, #8bc34a 0 50%, #0e8fc4 50%); }
  .dose-dot { left: 232px; width: 12px; height: 12px; border-radius: 50%; }
  .risk { left: 264px; width: 180px; height: 37px; border-radius: 2px; color: #fff; display: flex; align-items: center; padding-left: 12px; gap: 8px; }
  .risk-pct { font-family: "Raleway", sans-serif; font-weight: 300; font-size: 18px; }
  .risk-head { font-weight: 700; font-size: 10px; }
  .risk-sub { font-style: italic; font-weight: 700; font-size: 6.5px; line-height: 1.1; }

  /* slide 2 */
  .donut-label { width: 130px; text-align: center; top: 105px; font-size: 8.5px; font-weight: 700; color: var(--brand-red); }
  .donuts { left: 0; top: 125px; }
  .note { left: 41px; top: 240px; width: 480px; font-size: 10.5px; color: var(--brand-red); line-height: 1.3; }

  /* slide 3 */
  .case-box { left: 53px; top: 86px; width: 299px; height: 102px; background: var(--gold); color: #fff; font-family: "Open Sans", sans-serif; font-size: 8px; line-height: 1.45; padding: 9px 10px; }
  .case-more { left: 58px; top: 197px; width: 285px; color: var(--brand-red); font-family: "Open Sans", sans-serif; font-size: 8px; line-height: 1.45; }
  .bulb-art { left: 393px; top: 74px; width: 126px; height: 211px; border-radius: 63px 63px 20px 20px; background: linear-gradient(180deg, #ffff00 0%, #ffd400 60%, #444 78%, #333 100%); }

  /* slide 4 */
  .option { left: 39px; width: 509px; height: 35px; display: flex; background: var(--gold); color: #fff; font-size: 7.5px; }
  .option-key { width: 41px; background: var(--steel); display: flex; align-items: center; padding-left: 13px; }
  .option-text { flex: 1; display: flex; align-items: center; padding: 0 16px; line-height: 1.3; }
  .option.is-answer .option-text { font-weight: 700; }

  /* slide 5 */
  .quad { height: 48px; background: var(--teal); color: #fff; font-size: 7.8px; line-height: 1.35; padding: 0 18px; display: flex; align-items: center; }
  .quad.is-strong { font-weight: 700; }
  .axes { left: 225px; top: 95px; }
</style>
</head>
<body>
<div class="board">
  <h1 class="board-title">POWERPOINT SLIDE DESIGN IDEAS</h1>

  <!-- Consequences -->
  <section class="slide" style="left:7px; top:141px;">
    <h2 class="slide-title">CONSEQUENCES OF MULTIPLE MEDICATION USE</h2>
    <div class="brand"><span class="brand-mark"></span>Harlow Bureau of Wellness</div>
    <div class="rule"></div>
    <p class="lede">The use of several medications simultaneously, even at otherwise appropriate doses, increases the risk of adverse effects, drug interactions, non-adherence, and death.</p>
    <div class="figure-art" role="img" aria-label="Illustration of a human figure built from coloured puzzle pieces"></div>
    <div class="dose-dot" style="top:150px; background:#12a39a;"></div>
    <div class="dose-dot" style="top:189px; background:#12a39a;"></div>
    <div class="dose-dot" style="top:228px; background:#9e9e9e;"></div>
    <div class="risk" style="top:129px; background:var(--amber);"><span class="risk-pct">13%</span><div><div class="risk-head">RISK of ADRs</div><div class="risk-sub">When taking 2 medicines</div></div></div>
    <div class="risk" style="top:180px; background:var(--sky);"><span class="risk-pct">58%</span><div><div class="risk-head">RISK of ADRs</div><div class="risk-sub">When taking 5 medicines</div></div></div>
    <div class="risk" style="top:229px; background:var(--brand-red);"><span class="risk-pct">82%</span><div><div class="risk-head">RISK of ADRs</div><div class="risk-sub">When taking 7 medicines (Marlow 2015)</div></div></div>
    <footer class="footer"><span class="page">2</span><span>www.hlb.example-gov.org</span></footer>
  </section>

  <!-- Drug classes -->
  <section class="slide" style="left:607px; top:141px;">
    <h2 class="slide-title">DRUG CLASSES MOST COMMONLY INVOLVED IN ADRS</h2>
    <div class="brand"><span class="brand-mark"></span>Harlow Bureau of Wellness</div>
    <div class="rule"></div>
    <p class="lede">ADRs during hospitalization</p>
    <div class="donut-label" style="left:64px;">Cardiovascular Agents</div>
    <div class="donut-label" style="left:224px;">Analgesic Medications</div>
    <div class="donut-label" style="left:359px;">Anti-diabetic Drugs</div>
    <svg class="donuts" width="585" height="100" viewBox="0 0 585 100">
      <g font-family="Arimo, Arial, sans-serif" font-weight="700" font-size="14" text-anchor="middle">
        <g transform="translate(129 49)">
          <circle r="40" fill="none" stroke="var(--yellow)" stroke-width="12"/>
          <circle r="40" fill="none" stroke="var(--brand-red)" stroke-width="12" stroke-dasharray="85.4 251.3" transform="rotate(-90)"/>
          <text y="5" fill="var(--sky)">34%</text>
        </g>
        <g transform="translate(289 49)">
          <circle r="39" fill="none" stroke="var(--green)" stroke-width="9"/>
          <circle r="39" fill="none" stroke="var(--brand-red)" stroke-width="9" stroke-dasharray="44.1 245" transform="rotate(-90)"/>
          <text y="5" fill="var(--sky)">18%</text>
        </g>
        <g transform="translate(424 49)">
          <circle r="39" fill="none" stroke="var(--cyan)" stroke-width="9"/>
          <circle r="39" fill="none" stroke="var(--brand-red)" stroke-width="9" stroke-dasharray="24.5 245" transform="rotate(-90)"/>
          <text y="5" fill="var(--sky)">10%</text>
        </g>
      </g>
    </svg>
    <p class="note">Predictors of ADRs included the number of medications, use of hypoglycaemic agents, history of hyperlipidaemia, raised white cell count on admission and length of stay. (Okafor 2012)</p>
    <footer class="footer"><span class="page">4</span><span>www.hlb.example-gov.org</span></footer>
  </section>

  <!-- Case study 3, facts -->
  <section class="slide" style="left:7px; top:488px;">
    <h2 class="slide-title">CASE STUDY 3 - INSOMNIA</h2>
    <div class="brand"><span class="brand-mark"></span>Harlow Bureau of Wellness</div>
    <div class="rule"></div>
    <p class="case-box">A 79 yo female presents to clinic for general follow-up. On a comprehensive medication review, you identify that she is taking “nodrest” occasionally (an over the counter sleep aid containing diphenhydramine) and lorazepam each night prior to bedtime. She reports that she has taken the lorazepam “as long as I can remember” and uses the Nodrest to help her sleep through the night.</p>
    <p class="case-more">On further questioning, you learn that she has some anxiety in the evenings and started taking lorazepam decades ago when her late husband became ill. Now she is often able to go to sleep, but wakes up several times nightly to urinate. She finds the Nodrest helps her stay asleep through the night.</p>
    <div class="bulb-art" role="img" aria-label="Illustration of a light bulb assembled from coloured puzzle pieces"></div>
    <footer class="footer"><span class="page">9</span><span>www.hlb.example-gov.org</span></footer>
  </section>

  <!-- Case study 3, options -->
  <section class="slide" style="left:608px; top:488px;">
    <h2 class="slide-title">CASE STUDY 3 - INSOMNIA</h2>
    <div class="brand"><span class="brand-mark"></span>Harlow Bureau of Wellness</div>
    <div class="rule"></div>
    <p class="lede lede-bold">What should you do ?</p>
    <div class="option" style="top:101px;"><span class="option-key">a)</span><span class="option-text">Continue lorazepam, she has had no adverse effects thus far, discontinue Nodrest</span></div>
    <div class="option" style="top:143px;"><span class="option-key">b)</span><span class="option-text">Discontinue both medications immediately – their risk profiles outweigh any continued benefit</span></div>
    <div class="option" style="top:185px;"><span class="option-key">c)</span><span class="option-text">Discontinue both medications and instead prescribe a newer sleep aid like zolpidem. You know that benzodiazepines are bad.</span></div>
    <div class="option is-answer" style="top:228px;"><span class="option-key">d)</span><span class="option-text">Initiate taper off of lorazepam and stop nodrest. Discuss sleep hygiene, behavior modifying therapies to decrease nocturia and consider CBT if nocturnal anxiety returns.</span></div>
    <footer class="footer"><span class="page">11</span><span>www.hlb.example-gov.org</span></footer>
  </section>

  <!-- Medication reconciliation -->
  <section class="slide" style="left:317px; top:832px;">
    <h2 class="slide-title">MEDICATION RECONCILIATION</h2>
    <div class="brand"><span class="brand-mark"></span>Harlow Bureau of Wellness</div>
    <div class="rule"></div>
    <p class="lede lede-bold">What pharmaceuticals should be discontinued? Pharmaceuticals where:</p>
    <svg class="axes" width="140" height="140" viewBox="0 0 140 140">
      <g stroke="#222" stroke-width="2.5" fill="#222">
        <line x1="68" y1="8" x2="68" y2="132"/>
        <line x1="8" y1="70" x2="130" y2="70"/>
        <path d="M68 2 L63 10 L73 10 Z" stroke="none"/>
        <path d="M68 138 L63 130 L73 130 Z" stroke="none"/>
        <path d="M2 70 L10 65 L10 75 Z" stroke="none"/>
        <path d="M136 70 L128 65 L128 75 Z" stroke="none"/>
      </g>
    </svg>
    <div class="quad" style="left:37px; top:110px; width:249px;">Medication reconciliation process should be completed universally and regularly.</div>
    <div class="quad is-strong" style="left:300px; top:110px; width:242px;">Formal medication reviews at the time of discharge from the hospital (for patients with ten or more medication) or on a regular basis for outpatients.</div>
    <div class="quad" style="left:37px; top:170px; width:249px;">What medications are being used? What medications are being prescribed but not being used?</div>
    <div class="quad" style="left:300px; top:170px; width:242px;">To get honest answers, use non-accusatory language: “In the past month, how many doses of this medication did you take?”</div>
    <footer class="footer"><span class="page">13</span><span>www.hlb.example-gov.org</span></footer>
  </section>
</div>
</body>
</html>
```